Additional Benefits of Working for VALMIRA

Please prepare an infographic on the additional benefits besides salary of working at VALMIRA as detailed in the attached word document. Also attached is our logo in eps and our company design "Grounds". We are a Not For Profit company that finds jobs for unemployed people of government benefit payments

ShopCircle Market(s)

Attracting people to work for VALMIRA. Making VALMIRA an employer of choice.

Font styles to use
Sans Serif

Colors

Designer to choose colors to be used in the design.

Requirements
Must have
• be on 1 page
• have our logo
Nice to have
• Our Grounds design worked into it.
• Happy engaged employees
• Community engagement - we are a not for profit organisation
Should not have
• Discrimination, swearing,

```html
<!DOCTYPE html>
<html lang="en">
<head>
<meta charset="utf-8">
<title>The Benefits of Working with Us – VALMIRA</title>
<link href="https://fonts.googleapis.com/css2?family=Roboto:wght@400;700;900&display=swap" rel="stylesheet">
<style>
  :root {
    --black: #000000;
    --white: #ffffff;
    --lime: #8dc63f;
    --card-top: #3aa535;
    --card-bottom: #1d7a1f;
    --brand-dark: #111111;
  }
  * { margin: 0; padding: 0; box-sizing: border-box; }
  html, body { width: 1200px; height: 892px; overflow: hidden; background: var(--white); }
  body { font-family: "Roboto", Arial, sans-serif; }

  .canvas { position: relative; width: 1200px; height: 892px; background: var(--white); overflow: hidden; }

  .header-band {
    position: absolute; left: 0; top: 0; width: 598px; height: 138px;
    background: var(--black);
  }
  .header-title {
    position: absolute; left: 104px; top: 16px;
    color: var(--white); font-weight: 900; font-size: 53px; line-height: 52px;
    letter-spacing: 0.2px;
  }
  .brand {
    position: absolute; left: 820px; top: 58px; width: 180px;
    display: flex; align-items: center; gap: 8px;
  }
  .brand-dot { width: 16px; height: 16px; border-radius: 50%; background: var(--lime); }
  .brand-name {
    font-weight: 900; font-size: 40px; color: var(--brand-dark); letter-spacing: -0.5px;
    text-transform: lowercase;
  }
  .header-rule {
    position: absolute; left: 0; top: 138px; width: 1200px; height: 10px; background: var(--lime);
  }
  .footer-band {
    position: absolute; left: 0; top: 870px; width: 1200px; height: 22px; background: var(--black);
  }

  .card {
    position: absolute; width: 547px; height: 148px;
    background: linear-gradient(180deg, var(--card-top), var(--card-bottom));
    border-radius: 4px;
    box-shadow: 2px 3px 5px rgba(0,0,0,0.35);
  }
  .col-left { left: 40px; }
  .col-right { left: 615px; }
  .row-1 { top: 172px; }
  .row-2 { top: 349px; }
  .row-3 { top: 523px; }
  .row-4 { top: 696px; }

  .card-photo {
    position: absolute; left: 0; top: 0; width: 167px; height: 148px;
    border: 5px solid var(--lime); border-radius: 4px;
  }
  .card-photo .fill { width: 100%; height: 100%; }

  .card-body { position: absolute; left: 180px; top: 10px; right: 12px; color: var(--white); }
  .card-heading {
    display: flex; align-items: center; gap: 8px;
    font-weight: 700; font-size: 16.5px; margin-bottom: 6px;
  }
  .card-heading svg { width: 18px; height: 14px; flex: none; }
  .card-list { list-style: none; font-size: 11.6px; line-height: 15.3px; }
  .card-list li { padding-left: 12px; text-indent: -8px; }
  .card-list li::before { content: "- "; }

  .photo-party   { background: linear-gradient(135deg, #6b3a2a, #c0603a 55%, #3a2a22); }
  .photo-woman   { background: linear-gradient(160deg, #f1f1f1, #d8d0c8 60%, #2a2a2a); }
  .photo-gym     { background: linear-gradient(135deg, #3a3f48, #8a7a6a 55%, #2a2a2a); }
  .photo-volunteer { background: linear-gradient(160deg, #9ab07a, #4f8ccf 55%, #6a7a4a); }
  .photo-laptop  { background: linear-gradient(135deg, #f4f4f4, #d9dde0 55%, #b8c8c8); }
  .photo-award   { background: linear-gradient(160deg, #eeeeee, #c9c4bc 50%, #2b3550); }
  .photo-cash    { background: linear-gradient(135deg, #6a7a5a, #3a3f44 55%, #7a8a5a); }
  .photo-team    { background: linear-gradient(160deg, #7c8790, #a9a49c 55%, #5a6670); }
</style>
</head>
<body>
<div class="canvas">
  <div class="header-band">
    <h1 class="header-title">The Benefits of<br>Working with Us</h1>
  </div>
  <div class="brand"><span class="brand-dot"></span><span class="brand-name">valmira</span></div>
  <div class="header-rule"></div>

  <svg width="0" height="0" style="position:absolute">
    <defs>
      <symbol id="turn-arrow" viewBox="0 0 18 14">
        <path d="M1 13 C5 13 6 10 8 7 C10 4 12 3 15 3" fill="none" stroke="#fff" stroke-width="2" stroke-linecap="round"/>
        <path d="M12 0.5 L16.5 3 L12.5 6" fill="none" stroke="#fff" stroke-width="2" stroke-linecap="round" stroke-linejoin="round"/>
      </symbol>
    </defs>
  </svg>

  <section class="card col-left row-1">
    <div class="card-photo"><div class="fill photo-party" role="img" aria-label="Photo of colleagues raising glasses in a toast"></div></div>
    <div class="card-body">
      <h2 class="card-heading"><svg><use href="#turn-arrow"/></svg>Life Balance</h2>
      <ul class="card-list">
        <li>VALMIRA Day Leave. An extra day off at Christmas!</li>
        <li>Birthday Leave. A paid day off on your birthday</li>
        <li>A day off every month as Time In Lieu</li>
        <li>4 weeks Annual Leave</li>
        <li>Generous Personal Leave</li>
        <li>Support for parental leave for the birth or adoption of a child</li>
        <li>Flexible work arrangements</li>
      </ul>
    </div>
  </section>

  <section class="card col-right row-1">
    <div class="card-photo"><div class="fill photo-woman" role="img" aria-label="Photo of a smiling employee making an OK hand sign"></div></div>
    <div class="card-body">
      <h2 class="card-heading"><svg><use href="#turn-arrow"/></svg>Benefits</h2>
      <ul class="card-list">
        <li>Discounted vouches for Grocera, FreshMart, SoundHub, CinemaLux, Cellar Co, ValueBarn, ShopCircle, OutdoorPro and many others via PayNest e-wallet</li>
        <li>A range of other employee discounts are also available, including access to discounted banking and finance, vehicle purchasing, leasing and hotel accommodation</li>
      </ul>
    </div>
  </section>

  <section class="card col-left row-2">
    <div class="card-photo"><div class="fill photo-gym" role="img" aria-label="Photo of people on exercise bikes at a gym"></div></div>
    <div class="card-body">
      <h2 class="card-heading"><svg><use href="#turn-arrow"/></svg>Wellbeing</h2>
      <ul class="card-list">
        <li>Up to $450 per year to spend on Wellbeing services such as gym or yoga memberships</li>
        <li>Free counselling services 24x7 via our Employee Assistance Program</li>
        <li>Discount private health insurance</li>
        <li>WHS policies which support a safe, inclusive work place</li>
      </ul>
    </div>
  </section>

  <section class="card col-right row-2">
    <div class="card-photo"><div class="fill photo-volunteer" role="img" aria-label="Photo of volunteers collecting litter in a park"></div></div>
    <div class="card-body">
      <h2 class="card-heading"><svg><use href="#turn-arrow"/></svg>Contributing to Community</h2>
      <ul class="card-list">
        <li>Team involvement in local charity and community events</li>
        <li>Participation in VALMIRA's 1000 Jobs in 100 days initiative</li>
        <li>Strong relationships and connection with Indigenous Communities in support of Indigenous Employment</li>
      </ul>
    </div>
  </section>

  <section class="card col-left row-3">
    <div class="card-photo"><div class="fill photo-laptop" role="img" aria-label="Photo of hands working at a laptop on a desk"></div></div>
    <div class="card-body">
      <h2 class="card-heading"><svg><use href="#turn-arrow"/></svg>Career Growth &amp; Professional Development</h2>
      <ul class="card-list">
        <li>Ongoing internal training and development opportunities.</li>
        <li>External study support &amp; study leave</li>
        <li>Access to the tools and technology to do your job well</li>
        <li>Career advancement opportunities</li>
        <li>Internal job vacancy listings</li>
      </ul>
    </div>
  </section>

  <section class="card col-right row-3">
    <div class="card-photo"><div class="fill photo-award" role="img" aria-label="Photo of an employee in a suit wearing an award ribbon"></div></div>
    <div class="card-body">
      <h2 class="card-heading"><svg><use href="#turn-arrow"/></svg>Recognition</h2>
      <ul class="card-list">
        <li>We celebrate our people for reaching service milestones</li>
        <li>Team &amp; individual recognition for high performance</li>
      </ul>
    </div>
  </section>

  <section class="card col-left row-4">
    <div class="card-photo"><div class="fill photo-cash" role="img" aria-label="Photo of banknotes placed in a jacket pocket"></div></div>
    <div class="card-body">
      <h2 class="card-heading"><svg><use href="#turn-arrow"/></svg>Remuneration &amp; Salary Packaging</h2>
      <ul class="card-list">
        <li>Competitive salary</li>
        <li>Ability to salary package up to $15,900 and reduce your tax. Package rent, home loans, child care and much more</li>
        <li>Salary package up to $2,650 on meal entertainment and holiday accommodation</li>
      </ul>
    </div>
  </section>

  <section class="card col-right row-4">
    <div class="card-photo"><div class="fill photo-team" role="img" aria-label="Photo of three diverse colleagues standing together"></div></div>
    <div class="card-body">
      <h2 class="card-heading"><svg><use href="#turn-arrow"/></svg>Diversity &amp; Inclusion</h2>
      <ul class="card-list">
        <li>An inclusive and diverse culture where different backgrounds, experiences and perspectives are valued</li>
        <li>Gender diversity. Over 50% of our workforce and our leaders are female.</li>
      </ul>
    </div>
  </section>

  <div class="footer-band"></div>
</div>
</body>
</html>
```